Engineering Consultant Business Card

I'm starting a new business as a high-end engineering consultant in a niche field. I've attached the jpg for my logo plus the branding guideline document that I've been following. You can see my business website here: www.tarvikworks.com
I'd like a business card that has the logo on one side, then the other side has (in any order): Tarvik Works, Inc.
Dana Whitlock
President and Chief EMC Engineer
www.tarvikworks.com
dana@tarvikworks.com
Optional: motto "We will solve your EMC problems as early as possible—ideally before they even start."
I'm not planning on including a phone number
Target Market(s)
Businesses, especially makers of electronics hardware
Industry/Entity Type
Electrical engineering
Contact Information for Business Card
Company name, my name, website, email

```html
<!DOCTYPE html>
<html lang="en">
<head>
<meta charset="utf-8">
<title>Tarvik Works, Inc. — Business Card</title>
<link href="https://fonts.googleapis.com/css2?family=Red+Hat+Display:wght@500;700&family=Libre+Baskerville:wght@400;700&display=swap" rel="stylesheet">
<style>
  :root {
    --page: #9c9ea3;
    --brand-blue: #30479a;
    --ink-blue: #2e3f8f;
    --paper: #eef6f9;
    --trace: #14aacc;
    --white: #ffffff;
  }
  * { margin: 0; padding: 0; box-sizing: border-box; }
  html, body { width: 1200px; height: 1200px; overflow: hidden; }
  body { background: var(--page); position: relative; }

  .card {
    position: absolute;
    left: 183px;
    width: 819px;
    height: 470px;
    overflow: hidden;
  }
  .card--front { top: 90px; background: var(--brand-blue); }
  .card--back  { top: 624px; background: var(--paper); }

  .trace-field { position: absolute; }
  .card--front .trace-field {
    background: linear-gradient(90deg, rgba(20,170,204,0.10), rgba(20,170,204,0.28));
  }
  .trace-field--left  { left: 49px;  top: 102px; width: 255px; height: 282px; }
  .trace-field--top   { left: 407px; top: 39px;  width: 323px; height: 52px; }
  .trace-field--right { left: 772px; top: 140px; width: 47px;  height: 180px; }
  .card--back .trace-field--panel {
    left: 457px; top: 0; width: 362px; height: 470px;
    background: linear-gradient(135deg, rgba(20,170,204,0.08), rgba(20,170,204,0.22));
  }

  .chip { position: absolute; left: 304px; top: 91px; width: 468px; height: 279px; }
  .chip svg { position: absolute; inset: 0; }
  .chip__mark {
    position: absolute; inset: 0;
    display: flex; align-items: center; justify-content: center; gap: 22px;
  }
  .chip__dot {
    width: 62px; height: 62px; border-radius: 50%;
    border: 9px solid var(--brand-blue);
  }
  .chip__name {
    font-family: "Red Hat Display", sans-serif;
    font-weight: 700; font-size: 78px; letter-spacing: 2px;
    color: var(--brand-blue); line-height: 1;
  }

  .tagline {
    position: absolute; left: 304px; width: 468px; top: 377px;
    text-align: center; color: var(--white);
    font-family: "Red Hat Display", sans-serif; font-weight: 500;
    font-size: 22px; line-height: 28px;
  }

  .company {
    position: absolute; left: 48px; top: 50px;
    font-family: "Red Hat Display", sans-serif; font-weight: 700;
    font-size: 56px; line-height: 1; color: var(--ink-blue);
    letter-spacing: -0.5px;
  }
  .person {
    position: absolute; left: 48px; top: 236px;
    font-family: "Red Hat Display", sans-serif; font-weight: 700;
    font-size: 50px; line-height: 1; color: var(--ink-blue);
    padding-bottom: 10px; border-bottom: 3px solid var(--ink-blue);
  }
  .role, .contact {
    position: absolute; left: 48px;
    font-family: "Libre Baskerville", serif; color: var(--ink-blue);
  }
  .role { top: 306px; font-size: 19px; }
  .contact--email { top: 355px; font-size: 24px; }
  .contact--web { top: 390px; font-size: 24px; font-weight: 700; }
</style>
</head>
<body>

<section class="card card--front">
  <div class="trace-field trace-field--left" role="img" aria-label="Circuit board traces leading into the chip"></div>
  <div class="trace-field trace-field--top" role="img" aria-label="Row of circuit pins above the chip"></div>
  <div class="trace-field trace-field--right" role="img" aria-label="Circuit traces leaving the chip to the right"></div>

  <div class="chip">
    <svg width="468" height="279" viewBox="0 0 468 279" aria-hidden="true">
      <polygon points="64,0 468,0 468,279 0,279 0,46" fill="var(--paper)"/>
    </svg>
    <div class="chip__mark">
      <span class="chip__dot"></span>
      <span class="chip__name">TWI</span>
    </div>
  </div>

  <p class="tagline">Here to solve your EMC problems<br>--ideally before they even start</p>
</section>

<section class="card card--back">
  <div class="trace-field trace-field--panel" role="img" aria-label="Circuit board traces and pads"></div>

  <h1 class="company">Tarvik Works, Inc.</h1>
  <h2 class="person">Dana Whitlock</h2>
  <p class="role">President and Chief EMC Engineer</p>
  <p class="contact contact--email">dana@tarvikworks.com</p>
  <p class="contact contact--web">www.tarvikworks.com</p>
</section>

</body>
</html>
```